I need a business Card Design for my practice , i am clinical herbalist. I am a herbalist specializing in Lyme disease, autism, autoimmune diseases, difficult to cure diseasesDifficult to cure diseases. In my innovative practice i link traditional medicine, herbs with science, immunologu ,pharmacology.

Industry/Entity Type

Business

Contact Information for Business Card

My company name : OŚRODEK ZIELNIK
My name : Piotr Kaleta
Name of my profession : Fitoterapeuta
In Polish language Fitoterapeuta is Herbalist .

e-mail: piotrkaleta@osrodekzielnik.com
www.osrodek-zielnik.pl
phone : 604 587 231
My company adress : Dąbrowa Sitnicka 41 , 38-415 Lużna
I dont have logo .

Requirements
Nice to have
• My company

```html
<!DOCTYPE html>
<html lang="pl">
<head>
<meta charset="utf-8">
<title>Ośrodek Zielnik – wizytówka</title>
<link rel="stylesheet" href="https://fonts.googleapis.com/css2?family=Alfa+Slab+One&family=Quicksand:wght@500;700&display=swap">
<style>
  :root {
    --bg-light: #9aa6ab;
    --bg-dark: #4d575c;
    --card-dark: #1b1f27;
    --red: #ed1a36;
    --red-2: #d5152e;
    --red-3: #c31129;
    --red-4: #ae0d23;
    --icon-red: #8c0b1c;
    --ink: #141414;
    --white: #ffffff;
  }
  * { margin: 0; padding: 0; box-sizing: border-box; }
  html, body { width: 1200px; height: 900px; overflow: hidden; }
  body {
    background: radial-gradient(ellipse at 50% 40%, var(--bg-light), var(--bg-dark));
    position: relative;
  }
  .card {
    position: absolute;
    left: 120px; top: 175px;
    width: 960px; height: 549px;
    background: var(--card-dark);
    box-shadow: 0 20px 50px rgba(0,0,0,.35);
  }
  .card-shapes { position: absolute; inset: 0; width: 100%; height: 100%; }
  .company {
    position: absolute;
    left: 40px; top: 62px;
    width: 340px;
    text-align: center;
    font-family: "Alfa Slab One", serif;
    font-weight: 400;
    font-size: 46px;
    line-height: 1.12;
    color: var(--white);
    letter-spacing: .5px;
  }
  .person {
    position: absolute;
    right: 96px; top: 150px;
    text-align: right;
    font-family: "Quicksand", sans-serif;
    color: var(--ink);
  }
  .person-name { font-size: 30px; font-weight: 700; line-height: 1.1; }
  .person-role { font-size: 19px; font-weight: 500; margin-top: 2px; }
  .contacts {
    position: absolute;
    right: 28px; top: 300px;
    list-style: none;
    font-family: "Quicksand", sans-serif;
    font-weight: 500;
    font-size: 22px;
    color: var(--ink);
  }
  .contact-item {
    display: flex;
    align-items: center;
    justify-content: flex-end;
    gap: 14px;
    min-height: 42px;
    text-align: right;
    line-height: 1.25;
  }
  .contact-icon { width: 30px; height: 30px; flex: none; }
</style>
</head>
<body>
  <div class="card">
    <svg class="card-shapes" viewBox="0 0 960 549" aria-hidden="true">
      <polygon points="384,181 941,11 941,532 29,532 29,511" fill="var(--red)"/>
      <polygon points="384,181 29,511 29,532 120,532" fill="var(--red-2)"/>
      <polygon points="384,181 120,532 210,532" fill="var(--red-3)"/>
      <polygon points="384,181 210,532 298,532" fill="var(--red-4)"/>
    </svg>

    <h1 class="company">OŚRODEK<br>ZIELNIK</h1>

    <div class="person">
      <p class="person-name">Piotr Kaleta</p>
      <p class="person-role">Fitoterapeuta</p>
    </div>

    <ul class="contacts">
      <li class="contact-item">
        <span>604 587 231</span>
        <svg class="contact-icon" viewBox="0 0 30 30" aria-label="telefon">
          <circle cx="15" cy="15" r="15" fill="var(--icon-red)"/>
          <path d="M10 8.5l3 0 1.2 3.5-1.8 1.2a8 8 0 0 0 3.4 3.4l1.2-1.8 3.5 1.2 0 3a1.5 1.5 0 0 1-1.6 1.5A12 12 0 0 1 8.5 10.1 1.5 1.5 0 0 1 10 8.5z" fill="var(--white)"/>
        </svg>
      </li>
      <li class="contact-item">
        <span>piotrkaleta@osrodekzielnik.com</span>
        <svg class="contact-icon" viewBox="0 0 30 30" aria-label="e-mail">
          <circle cx="15" cy="15" r="15" fill="var(--icon-red)"/>
          <rect x="8" y="10" width="14" height="10" fill="var(--white)"/>
          <path d="M8 10l7 5.5 7-5.5" fill="none" stroke="var(--icon-red)" stroke-width="1.4"/>
        </svg>
      </li>
      <li class="contact-item">
        <span>www.osrodek-zielnik.pl</span>
        <svg class="contact-icon" viewBox="0 0 30 30" aria-label="strona internetowa">
          <circle cx="15" cy="15" r="15" fill="var(--icon-red)"/>
          <g fill="none" stroke="var(--white)" stroke-width="2" stroke-linecap="round">
            <rect x="7.5" y="12" width="9" height="6" rx="3"/>
            <rect x="13.5" y="12" width="9" height="6" rx="3"/>
          </g>
        </svg>
      </li>
      <li class="contact-item">
        <span>Dąbrowa Sitnicka 41<br>38-415 Lużna</span>
        <svg class="contact-icon" viewBox="0 0 30 30" aria-label="adres">
          <circle cx="15" cy="15" r="15" fill="var(--icon-red)"/>
          <path d="M15 23s-5.5-6-5.5-9.5a5.5 5.5 0 0 1 11 0C20.5 17 15 23 15 23z" fill="var(--white)"/>
          <circle cx="15" cy="13.5" r="2" fill="var(--icon-red)"/>
        </svg>
      </li>
    </ul>
  </div>
</body>
</html>
```